Build Distinctive Business Card: Public Relations Government Relations firm

I have logo and colors done (attached) need a very cool way to present it on a business card (can be two sided if need be).

Public Relations Government Relations firm

Info:

Mark Tillson, CEO
Keystone Public Relations
2786 West Harlow Blvd.
Los Angeles CA 90047
(o) 213.555.0148
(f) 213.555.0193
mark@keystonekpr-example.com

Target Market(s)

Government relations, public relations, lobbyist, I was a past State Senator

Industry/Entity Type

Business

Contact Information for Business Card

Info:

Mark Tillson, CEO
Keystone Public Relations
2786 West Harlow Blvd.
Los Angeles CA 90047
(o) 213.555.0148
(f) 213.555.0193
mark@keystonekpr-example.com
@marktillson

Requirements
Must have
• A sense of balance given logo is already done.
• It's a government relations firm really.
• Lobbyist type.
• Senatorial type...

```html
<!DOCTYPE html>
<html lang="en">
<head>
<meta charset="utf-8">
<title>Keystone Public Relations – Business Card</title>
<link rel="stylesheet" href="https://fonts.googleapis.com/css2?family=Open+Sans:wght@400;600&display=swap">
<style>
  :root {
    --brand-blue: #1a9ad6;
    --brand-blue-deep: #0d7fbf;
    --ink: #2a2a2a;
    --rule: #9a9a9a;
    --card: #ffffff;
    --backdrop: #e9e9e9;
  }
  * { margin: 0; padding: 0; box-sizing: border-box; }
  html, body { width: 1200px; height: 885px; overflow: hidden; }
  body {
    background: var(--backdrop);
    font-family: "Open Sans", Arial, sans-serif;
    position: relative;
  }
  .card {
    position: absolute;
    width: 560px;
    height: 320px;
    background: var(--card);
    border-radius: 16px;
    box-shadow: 0 6px 18px rgba(0,0,0,0.18);
    overflow: hidden;
  }
  .card--front { left: 50px; top: 110px; }
  .card--back { left: 590px; top: 455px; }

  /* Front */
  .front-brand {
    position: absolute;
    left: 0; top: 0;
    width: 280px; height: 320px;
    display: flex; align-items: center; justify-content: center; gap: 12px;
  }
  .brand-dot {
    width: 46px; height: 46px; border-radius: 50%;
    background: var(--brand-blue);
    flex: none;
  }
  .brand-name {
    color: var(--brand-blue);
    font-weight: 600;
    font-size: 19px;
    line-height: 1.15;
  }
  .front-divider {
    position: absolute;
    left: 280px; top: 55px;
    width: 1px; height: 210px;
    background: var(--rule);
  }
  .contact {
    position: absolute;
    left: 306px; top: 62px;
    color: var(--ink);
    font-size: 14px;
    line-height: 1.35;
  }
  .contact__name {
    color: var(--brand-blue);
    font-size: 26px;
    font-weight: 400;
    line-height: 1.1;
  }
  .contact__title { font-size: 15px; margin-bottom: 22px; }
  .contact__address { margin-bottom: 4px; }
  .contact__line { display: flex; align-items: center; gap: 8px; height: 21px; }
  .icon { width: 15px; height: 15px; flex: none; }

  /* Back */
  .back-name {
    position: absolute;
    left: 36px; top: 42px;
    color: var(--brand-blue);
    font-weight: 600;
    font-size: 30px;
    line-height: 1.1;
  }
  .back-circle {
    position: absolute;
    left: 250px; top: 90px;
    width: 360px; height: 360px;
    border-radius: 50%;
    background: linear-gradient(160deg, var(--brand-blue) 0%, var(--brand-blue-deep) 100%);
  }
</style>
</head>
<body>

<section class="card card--front">
  <div class="front-brand">
    <span class="brand-dot"></span>
    <span class="brand-name">Keystone<br>Public Relations</span>
  </div>
  <div class="front-divider"></div>
  <div class="contact">
    <p class="contact__name">Mark Tillson</p>
    <p class="contact__title">CEO</p>
    <p class="contact__address">2786 West Harlow Blvd.<br>Los Angeles CA 90047</p>
    <p class="contact__line">
      <svg class="icon" viewBox="0 0 16 16" aria-hidden="true"><rect width="16" height="16" rx="2" fill="var(--brand-blue)"/><path d="M4.5 3.5c1 2.2 1.6 2.9 2 3.3l-1 1c.8 1.6 2 2.8 3.5 3.6l1-1c.4.3 1.1.9 3 1.9l-.8 1.6C7.6 13.5 2.8 8.8 2.7 4.4z" fill="#fff"/></svg>
      213.555.0148
    </p>
    <p class="contact__line">
      <svg class="icon" viewBox="0 0 16 16" aria-hidden="true"><rect width="16" height="16" rx="2" fill="var(--brand-blue)"/><path d="M4.5 3.5c1 2.2 1.6 2.9 2 3.3l-1 1c.8 1.6 2 2.8 3.5 3.6l1-1c.4.3 1.1.9 3 1.9l-.8 1.6C7.6 13.5 2.8 8.8 2.7 4.4z" fill="#fff"/></svg>
      213.555.0193
    </p>
    <p class="contact__line">
      <svg class="icon" viewBox="0 0 16 16" aria-hidden="true"><rect width="16" height="16" rx="2" fill="var(--brand-blue)"/><rect x="3" y="4.5" width="10" height="7" fill="none" stroke="#fff" stroke-width="1.2"/><path d="M3 4.5l5 4 5-4M3 11.5l3.6-3.6M13 11.5L9.4 7.9" fill="none" stroke="#fff" stroke-width="1.1"/></svg>
      mark@keystonekpr-example.com
    </p>
  </div>
</section>

<section class="card card--back">
  <p class="back-name">Keystone<br>Public Relations</p>
  <div class="back-circle"></div>
</section>

</body>
</html>
```